Birchwell Hedge and Lawn Care Care Wrap

We have 3 White Marlow Trekkas (2 are from 2015 and 1 is 2017). We want them all to be branded, not necessarily a full vehicle wrap, but definite eye catching design with our logo prominently display along with our phone number 914-368-2957 and web address BirchwellHedgeCare.com. We are in the tree and plant care business, green is our main brand color.

Font styles to use
Sans Serif

Colors

Designer to choose colors to be used in the design.

Requirements
Must have
• MUST USED EXACT LOGO THAT WAS UPLOADED.
Nice to have
• Leaves along the bottom. Simple and easy to read.
Should not have
• DO NOT ADJUST OR CHANGE OUR LOGO.

```html
<!DOCTYPE html>
<html lang="en">
<head>
<meta charset="utf-8">
<title>Birchwell Hedge and Lawn Care – Vehicle Wrap</title>
<link rel="stylesheet" href="https://fonts.googleapis.com/css2?family=Archivo:ital,wght@0,800;1,800&display=swap">
<style>
  :root {
    --canvas: #f1f2f0;
    --wrap-white: #ffffff;
    --brand-green: #2f7d3c;
    --brand-green-deep: #1f6a2a;
    --brand-green-soft: #5e9e66;
    --label-gold: #a77f10;
    --rear-text: #f2f7f1;
  }
  * { box-sizing: border-box; margin: 0; padding: 0; }
  html, body { width: 688px; height: 1200px; overflow: hidden; }
  body {
    background: var(--canvas);
    font-family: "Archivo", Arial, sans-serif;
    position: relative;
  }

  /* Side panel */
  .side-panel {
    position: absolute;
    left: 40px; top: 70px;
    width: 608px; height: 400px;
    background: var(--wrap-white);
    border-radius: 14px;
    overflow: hidden;
    box-shadow: 0 2px 10px rgba(0,0,0,.08);
  }
  .side-panel .green-sweep {
    position: absolute; inset: 0;
    width: 100%; height: 100%;
  }

  .brand-mark {
    position: absolute;
    display: flex;
    align-items: center;
    gap: 10px;
    font-weight: 800;
  }
  .brand-mark .brand-square {
    flex: none;
    background: var(--brand-green);
  }
  .side-panel .brand-mark {
    left: 40px; top: 170px;
    width: 190px;
    font-size: 17px;
    line-height: 1.25;
    color: var(--brand-green-deep);
  }
  .side-panel .brand-square { width: 26px; height: 26px; }

  .contact-block {
    position: absolute;
    left: 248px; top: 78px;
    color: var(--brand-green-deep);
  }
  .web-address {
    font-weight: 800;
    font-size: 19px;
    margin-bottom: 22px;
  }
  .region { margin-bottom: 12px; }
  .region-label {
    color: var(--label-gold);
    font-weight: 800;
    font-size: 14px;
    line-height: 1.1;
  }
  .region-phone {
    font-weight: 800;
    font-size: 25px;
    line-height: 1.15;
  }

  /* Rear panel */
  .rear-panel {
    position: absolute;
    left: 40px; top: 530px;
    width: 608px; height: 600px;
    border-radius: 14px;
    overflow: hidden;
    background: linear-gradient(180deg, var(--brand-green-soft) 0%, var(--brand-green) 55%, var(--brand-green-deep) 100%);
    box-shadow: 0 2px 10px rgba(0,0,0,.08);
  }
  .rear-window {
    position: absolute;
    left: 60px; top: 50px;
    width: 488px; height: 170px;
    border-radius: 40px 40px 24px 24px;
    background: rgba(255,255,255,.14);
  }
  .rear-panel .brand-mark {
    right: 50px; top: 320px;
    width: 150px;
    font-size: 12px;
    line-height: 1.25;
    color: var(--rear-text);
    gap: 8px;
  }
  .rear-panel .brand-square { width: 18px; height: 18px; background: var(--rear-text); }
  .rear-phones {
    position: absolute;
    left: 60px; right: 60px; top: 450px;
    display: flex; justify-content: space-between;
    color: var(--rear-text);
    font-weight: 800;
    font-size: 24px;
  }
  .rear-web {
    position: absolute;
    right: 60px; top: 510px;
    color: var(--rear-text);
    font-weight: 800;
    font-style: italic;
    font-size: 24px;
  }
</style>
</head>
<body>

<section class="side-panel" aria-label="Side panel graphic">
  <svg class="green-sweep" viewBox="0 0 608 400" preserveAspectRatio="none" aria-hidden="true">
    <defs>
      <linearGradient id="sweepFade" x1="0" y1="0" x2="1" y2="0">
        <stop offset="0" stop-color="#2f7d3c" stop-opacity="0"/>
        <stop offset="0.4" stop-color="#2f7d3c" stop-opacity="0.35"/>
        <stop offset="1" stop-color="#2f7d3c" stop-opacity="1"/>
      </linearGradient>
    </defs>
    <polygon points="505,0 608,0 608,400 440,400" fill="url(#sweepFade)"/>
    <polygon points="555,0 608,0 608,400 500,400" fill="#2f7d3c"/>
  </svg>

  <div class="brand-mark">
    <span class="brand-square" aria-hidden="true"></span>
    <span class="brand-name">Birchwell Hedge and Lawn Care</span>
  </div>

  <div class="contact-block">
    <p class="web-address">BirchwellHedgeCare.com</p>
    <div class="region">
      <p class="region-label">Westchester</p>
      <p class="region-phone">914-368-2957</p>
    </div>
    <div class="region">
      <p class="region-label">Fairfield, CT</p>
      <p class="region-phone">203-517-8046</p>
    </div>
    <div class="region">
      <p class="region-label">New York City</p>
      <p class="region-phone">718-294-6130</p>
    </div>
  </div>
</section>

<section class="rear-panel" aria-label="Rear panel graphic">
  <div class="rear-window" aria-hidden="true"></div>
  <div class="brand-mark">
    <span class="brand-square" aria-hidden="true"></span>
    <span class="brand-name">Birchwell Hedge and Lawn Care</span>
  </div>
  <div class="rear-phones">
    <span>914-368-2957</span>
    <span>203-517-8046</span>
  </div>
  <p class="rear-web">BirchwellHedgeCare.com</p>
</section>

</body>
</html>
```